Brackendale Physiotherapy & Sports Injuries Clinic Flyer Design

At Brackendale Physiotherapy & Sports Injuries Clinic we are proud to treat each individual with a high level of care and as a whole person and not just as an injury. We look at identifying problems and setting goals in relation to each patient’s individual situation. Hands-on treatments, rehabilitation and education/advice are central to our approach and we offer clear and simple explanations to keep you fully informed of the nature of your problem, the prognosis and aims of treatment. The aim is to provide the best Physiotherapy and Sports Injuries Clinic in the Penrith & Brackendale area with a professional, caring and friendly approach

List of services:
Specialist Physiotherapy & Rehabilitation
Pilates & Back Care Classes
Sports Massage
Gait Analysis and Orthotics prescription
Sports Biomechanics and Corrective Exercise

Key points:
Professional, caring and friendly approach
Flexible appointment times
Conveniently located with paring just off M9 J27

Contact Joan the Physio
Tel: 07812093347
Email: info@brackendalephysio-demo.co.uk
Website www.brackendalephysio-demo.co.uk
Facebook www.facebook.com/brackendalephysio-demo.co.uk

Find us:
Brackendale Physiotherapy & Sports Injuries Clinic
Harrowmead Business Park
Penrith, Cumbria
CA227QD

```html
<!DOCTYPE html>
<html lang="en">
<head>
<meta charset="utf-8">
<title>Brackendale Physiotherapy &amp; Sports Injuries Clinic – Flyer</title>
<link rel="stylesheet" href="https://fonts.googleapis.com/css2?family=Noto+Sans:wght@700;800&display=swap">
<style>
  :root {
    --sky-light: #c9ecfb;
    --sky-mid: #8fd3f2;
    --royal: #1c3fd1;
    --royal-deep: #1633b8;
    --white: #ffffff;
    --ink: #1d3acb;
    --photo-warm: #e9e4d2;
    --photo-cool: #c9d6df;
  }
  html, body {
    margin: 0;
    padding: 0;
    width: 1200px;
    height: 930px;
    overflow: hidden;
    background: var(--white);
  }
  .flyer {
    position: relative;
    width: 1200px;
    height: 930px;
    overflow: hidden;
    font-family: "Noto Sans", Verdana, sans-serif;
    font-weight: 700;
    background: linear-gradient(180deg, var(--sky-mid) 0%, var(--sky-light) 45%, var(--sky-mid) 100%);
  }
  .backdrop {
    position: absolute;
    inset: 0;
  }
  .clinic-title {
    position: absolute;
    left: 42px;
    top: 22px;
    margin: 0;
    color: var(--white);
    font-size: 50px;
    line-height: 64px;
    font-weight: 800;
    letter-spacing: 0.2px;
  }
  .brand-name {
    position: absolute;
    left: 905px;
    top: 78px;
    margin: 0;
    color: var(--royal);
    font-size: 38px;
    font-weight: 800;
  }
  .tagline {
    position: absolute;
    left: 0;
    top: 182px;
    width: 1200px;
    height: 52px;
    margin: 0;
    display: flex;
    align-items: center;
    justify-content: center;
    color: var(--ink);
    font-size: 26px;
    letter-spacing: 0.3px;
  }
  .photo {
    position: absolute;
    left: 42px;
    width: 344px;
    border: 3px solid var(--white);
    box-shadow: 6px 6px 10px rgba(0, 0, 0, 0.45);
    box-sizing: border-box;
  }
  .photo--reception {
    top: 266px;
    height: 260px;
    background: linear-gradient(135deg, var(--photo-cool) 0%, var(--photo-warm) 55%, #b9c6d6 100%);
  }
  .photo--treatment {
    top: 546px;
    height: 282px;
    background: linear-gradient(160deg, var(--photo-warm) 0%, #d8dde4 50%, #5d6478 100%);
  }
  .headline {
    position: absolute;
    left: 446px;
    top: 256px;
    margin: 0;
    color: var(--white);
    font-size: 47px;
    font-weight: 800;
    letter-spacing: 0.5px;
  }
  .intro {
    position: absolute;
    left: 454px;
    top: 330px;
    width: 700px;
    margin: 0;
    color: var(--white);
    font-size: 21.5px;
    line-height: 31px;
  }
  .services {
    position: absolute;
    left: 454px;
    top: 546px;
    margin: 0;
    color: var(--ink);
    font-size: 24px;
    line-height: 36px;
  }
  .services__heading {
    margin: 0;
    font-size: 24px;
  }
  .services__list {
    list-style: none;
    margin: 0;
    padding: 0;
  }
  .services__list li::before {
    content: "•";
    display: inline-block;
    width: 24px;
  }
  .key-points {
    position: absolute;
    left: 0;
    top: 846px;
    width: 1200px;
    margin: 0;
    text-align: center;
    color: var(--ink);
    font-size: 25px;
  }
</style>
</head>
<body>
  <main class="flyer">
    <svg class="backdrop" width="1200" height="930" viewBox="0 0 1200 930" aria-hidden="true">
      <path d="M0,105 C260,112 560,140 760,182 L0,182 Z" fill="var(--royal)"/>
      <path d="M760,182 C900,150 1080,180 1200,230 L1200,182 Z" fill="var(--royal)" opacity="0.0"/>
      <rect x="0" y="182" width="1200" height="52" fill="var(--white)"/>
      <path d="M0,234 H1200 V470 C980,480 720,505 520,532 C320,558 140,560 0,548 Z" fill="var(--royal)"/>
      <path d="M1200,234 C1120,250 1060,268 1000,300 L1200,300 Z" fill="var(--royal-deep)"/>
      <path d="M0,548 C140,560 320,558 520,532 C720,505 980,480 1200,470 V808 C960,840 640,830 360,812 C200,802 80,800 0,806 Z" fill="var(--white)"/>
    </svg>

    <h1 class="clinic-title">Brackendale Physiotherapy<br>&amp; Sports Injuries Clinic</h1>
    <p class="brand-name">Brackendale</p>

    <p class="tagline">Treating each individual as a whole person and not just as an injury</p>

    <div class="photo photo--reception" role="img" aria-label="Photo of the clinic reception and waiting area with chairs, certificates on the wall and a flower pot"></div>
    <div class="photo photo--treatment" role="img" aria-label="Photo of the treatment room with a treatment couch, anatomy posters, desk and skeleton model"></div>

    <h2 class="headline">Physio - Rehab - Recovery</h2>
    <p class="intro">Brackendale Physiotherapy &amp; Sports Injuries<br>Clinic aims to be the best Physiotherapy,<br>sports massage and rehabilitation service<br>in the Brackendale and Penrith area with a<br>professional, caring and friendly approach.</p>

    <section class="services">
      <h3 class="services__heading">List of services:</h3>
      <ul class="services__list">
        <li>Sports Massage</li>
        <li>Specialist Physiotherapy &amp; Rehabilitation</li>
        <li>Pilates &amp; Back Care Classes</li>
        <li>Gait Analysis and Orthotics prescription</li>
        <li>Sports Biomechanics and Corrective Exercise</li>
      </ul>
    </section>

    <p class="key-points">Professional, caring and friendly approach - Flexible appointment times</p>
  </main>
</body>
</html>
```